WordPress Site Clean up

We are a small wireless networking company in Norther Colorado. We have a basic layout to our new website, and require a person or persons who can clean the new site up so we can go live with it in the coming weeks. Our company has the logo and content, we just need to clean the formatting up, improve the colors/graphics. It is currently a ZUNPLIKE. We also need help making our project pictures look better on the website, and clean up the images all around.

The website can be found at: www.4qvtelmora.com/newsite

We can provide you with photos and more content, but we have gone as far as we can with "building" the wordpress site.

It Company

```html
<!DOCTYPE html>
<html lang="en">
<head>
<meta charset="utf-8">
<title>Telmora Networks</title>
<link href="https://fonts.googleapis.com/css2?family=Bebas+Neue&family=Oswald:wght@300;400;500&family=Open+Sans:wght@400;600;700&display=swap" rel="stylesheet">
<style>
:root{
  --green:#8cc63e;
  --green-dark:#5d8a22;
  --ink:#1b2015;
  --ink-2:#23291c;
  --light:#dfe6c3;
  --light-2:#c9d69b;
  --text-light:#c7cdb8;
  --text-dark:#3a4030;
  --white:#ffffff;
}
*{box-sizing:border-box;margin:0;padding:0}
html,body{width:1200px;height:5099px;overflow:hidden}
body{font-family:"Open Sans",sans-serif;font-size:12px;color:var(--text-light);background:var(--ink);position:relative}
section,header,footer{position:absolute;left:0;width:1200px}
.wrap{position:absolute;left:150px;width:900px}
.center{text-align:center}
h2.section-title{font-family:"Oswald",sans-serif;font-weight:400;text-transform:uppercase;font-size:30px;letter-spacing:.5px;text-align:center}
.on-dark h2.section-title{color:var(--white)}
.on-light h2.section-title{color:#222}
.lead{font-size:12px;text-align:center;line-height:1.6}
.on-dark .lead{color:var(--text-light)}
.on-light .lead{color:var(--text-dark)}
.arrows{position:absolute;left:0;width:900px;display:flex;justify-content:center;gap:14px}
.arrow{width:44px;height:44px;background:#111;display:flex;align-items:center;justify-content:center}
.on-light .arrow{background:#b6c47e}
.dots{position:absolute;left:0;width:900px;display:flex;justify-content:center;gap:7px}
.dot{width:8px;height:8px;border-radius:50%;background:#5c6450}
.dot.on{background:var(--green)}
.photo{border:4px solid #e9eee0}

/* header */
.hero{top:0;height:646px;background:linear-gradient(180deg,#6f8a6b 0%,#4f6a45 35%,#3d5a2a 60%,#26361b 100%)}
.nav{position:absolute;top:0;left:150px;width:900px;height:60px;display:flex;align-items:center;justify-content:space-between}
.brand{font-family:"Oswald",sans-serif;font-size:26px;color:var(--white);display:flex;align-items:center;gap:8px}
.brand .mark{width:14px;height:14px;background:var(--green)}
.menu{display:flex;gap:2px;font-family:"Oswald",sans-serif;font-size:13px;text-transform:uppercase}
.menu a{color:var(--white);text-decoration:none;padding:6px 9px}
.menu a.active{background:var(--green)}
.hero h1{position:absolute;top:290px;left:0;width:1200px;text-align:center;font-family:"Bebas Neue",sans-serif;font-weight:400;font-size:80px;line-height:72px;color:var(--white)}
.hero .rule{position:absolute;top:452px;left:560px;width:80px;height:2px;background:var(--white)}
.hero .sub{position:absolute;top:470px;left:0;width:1200px;text-align:center;color:var(--white);font-family:"Oswald",sans-serif;text-transform:uppercase}
.hero .sub b{display:block;font-size:26px;font-weight:400}
.hero .sub span{font-size:13px;letter-spacing:1px}
.hero .down{position:absolute;top:582px;left:582px;width:36px;height:32px;background:var(--green);display:flex;align-items:center;justify-content:center}

/* intro */
.intro{top:646px;height:697px;background:var(--ink)}
.intro h2{position:absolute;top:70px;width:900px;font-size:30px;line-height:38px}
.cards{position:absolute;top:187px;left:0;width:900px;display:flex;gap:24px}
.card{width:284px}
.card .img{height:190px;background:linear-gradient(135deg,#dce8f4,#5d8fbf)}
.card h3{margin-top:30px;font-family:"Oswald",sans-serif;font-weight:400;font-size:17px;color:var(--green);text-transform:uppercase}
.card p{margin-top:8px;line-height:1.6;font-size:11px}

/* what we do */
.what{top:1343px;height:662px;background:radial-gradient(ellipse at 50% 40%,#eef2d8 0%,var(--light) 45%,var(--light-2) 100%)}
.what .brand-small{position:absolute;top:190px;left:0;width:900px;text-align:center;font-family:"Oswald",sans-serif;font-size:26px;color:#2c3324}
.features{position:absolute;top:280px;left:0;width:900px;display:flex;justify-content:space-between}
.feature{width:160px;text-align:center;color:var(--text-dark)}
.feature .icon{width:84px;height:84px;margin:0 auto;background:var(--green);display:flex;align-items:center;justify-content:center}
.feature:nth-child(even){margin-top:40px}
.feature h4{font-family:"Oswald",sans-serif;font-weight:400;font-size:15px;text-transform:uppercase;margin:14px 0 8px;color:#222}
.feature p{font-size:10px;line-height:1.55}

/* projects */
.projects{top:2005px;height:629px;background:var(--ink)}
.project .img{height:196px}
.project h3{margin-top:24px;font-size:17px;line-height:22px}
.project a{display:block;margin-top:8px;font-size:10px;color:var(--green)}

/* team */
.team{top:2634px;height:544px;background:linear-gradient(180deg,#e5e9c4,#cfd99e)}
.members{position:absolute;top:195px;left:0;width:900px;display:flex;justify-content:space-between;padding:0 40px}
.member{width:150px;text-align:center;color:var(--text-dark)}
.member .img{width:150px;height:156px;background:linear-gradient(180deg,#b9c2b5,#6d7767);border:4px solid #f4f6ea}
.member h5{margin-top:12px;font-family:"Oswald",sans-serif;font-weight:400;font-size:13px;text-transform:uppercase;color:#222}
.member small{display:block;font-size:9px;margin-top:2px}
.member .social{display:flex;justify-content:center;gap:6px;margin-top:6px}
.member .social i{width:9px;height:9px;background:#333;display:block}

/* banner */
.banner{top:3178px;height:204px;background:linear-gradient(90deg,#1f3212,#3e6b18 50%,#1f3212)}
.banner p{position:absolute;top:56px;left:150px;width:900px;font-family:"Oswald",sans-serif;font-size:25px;line-height:33px;text-transform:uppercase;color:var(--green);font-weight:400;text-align:center}

/* success */
.success{top:3382px;height:629px;background:linear-gradient(180deg,#15190f,#22281a)}
.success .person{position:absolute;top:153px;left:386px;width:128px;height:128px;background:linear-gradient(180deg,#c6ccc0,#6f7869)}
.success blockquote{position:absolute;top:300px;left:60px;width:780px;text-align:center;font-style:italic;font-size:11.5px;line-height:1.6;color:var(--text-light)}
.success cite{position:absolute;top:420px;left:0;width:900px;text-align:center;font-style:normal;font-size:11px;color:var(--green)}
.success cite small{display:block;color:var(--text-light);font-size:9px}

/* partners */
.partners{top:4011px;height:255px;background:var(--light)}
.badges{position:absolute;top:118px;left:0;width:900px;display:flex;justify-content:space-between;padding:0 10px}
.badge{width:124px;height:70px;background:var(--white);display:flex;align-items:center;justify-content:center}
.badge i{display:block;width:70px;height:26px;border-radius:4px;background:#c9cfc0}

/* contact */
.contact{top:4266px;height:765px;background:linear-gradient(180deg,#2b3f2a 0%,#48683b 40%,#31472a 75%,#1d2616 100%)}
.fields{position:absolute;top:197px;left:0;width:900px;display:flex;gap:20px}
.field{flex:1;height:34px;background:rgba(255,255,255,.22);color:#dfe4d3;font-size:10px;padding:10px 12px}
.message{position:absolute;top:255px;left:0;width:900px;height:153px;background:rgba(255,255,255,.22);color:#dfe4d3;font-size:10px;padding:10px 12px}
.send{position:absolute;top:455px;left:385px;width:130px;height:34px;background:var(--green);color:#1b2015;font-family:"Oswald",sans-serif;font-size:11px;text-transform:uppercase;display:flex;align-items:center;justify-content:center}
.info{position:absolute;top:560px;left:0;width:900px;display:flex;justify-content:space-between}
.info-item{width:270px;display:flex;gap:14px;color:var(--white);font-size:10px;line-height:1.5}
.info-item h6{font-family:"Oswald",sans-serif;font-weight:400;font-size:14px;text-transform:uppercase;margin-bottom:4px}

footer{top:5031px;height:68px;background:#10140b;color:#8a9179;font-size:10px}
footer .copy{position:absolute;left:150px;top:28px}
footer .social{position:absolute;right:150px;top:26px;display:flex;gap:10px}
footer .social i{width:12px;height:12px;border-radius:50%;background:#6d745f;display:block}
</style>
</head>
<body>

<header class="hero" role="img" aria-label="Misty green mountain ridge with forest beneath a cloudy sky">
  <nav class="nav">
    <div class="brand"><span class="mark"></span>Telmora Networks</div>
    <div class="menu">
      <a class="active">Home</a><a>About</a><a>Markets</a><a>Services</a><a>Products</a><a>Success Stories</a><a>Technologies</a><a>Contact</a>
    </div>
  </nav>
  <h1>All your wireless needs a<br>professional solution</h1>
  <div class="rule"></div>
  <div class="sub"><b>Complete Network</b><span>Communications Solution Provider</span></div>
  <div class="down"><svg width="14" height="10" viewBox="0 0 14 10"><path d="M1 2l6 6 6-6" stroke="#fff" stroke-width="2" fill="none"/></svg></div>
</header>

<section class="intro on-dark">
  <div class="wrap">
    <h2 class="section-title">Telmora Networks is a complete network communications solution<br><span style="font-size:22px">provider committed to delivering the highest level of customer satisfaction.</span></h2>
    <div class="cards">
      <div class="card"><div class="img photo" role="img" aria-label="Hand touching a glowing network interface"></div><h3>Our Services</h3><p>Providing world class service is our core commitment. We provide a whole host of services from installation to design work.</p></div>
      <div class="card"><div class="img photo" role="img" aria-label="Blue gears and network symbols"></div><h3>Our Solutions</h3><p>We are a total network solution provider. We carefully learn the needs of our customers and fit them with the right solution.</p></div>
      <div class="card"><div class="img photo" role="img" aria-label="People reviewing plans at a desk" style="background:linear-gradient(135deg,#f2f2ee,#9aa3ad)"></div><h3>Our Designs</h3><p>Designing networks is a combination of science, equipment and a little bit of art. Today's companies can rely on our design expertise.</p></div>
    </div>
    <div class="arrows" style="top:543px">
      <div class="arrow"><svg width="10" height="14"><path d="M8 1L2 7l6 6" stroke="#fff" stroke-width="2" fill="none"/></svg></div>
      <div class="arrow"><svg width="10" height="14"><path d="M2 1l6 6-6 6" stroke="#fff" stroke-width="2" fill="none"/></svg></div>
    </div>
    <div class="dots" style="top:600px"><i class="dot on"></i><i class="dot"></i><i class="dot"></i><i class="dot"></i></div>
  </div>
</section>

<section class="what on-light">
  <div class="wrap">
    <h2 class="section-title" style="position:absolute;top:40px;width:900px">What we do</h2>
    <div style="position:absolute;top:86px;left:400px;width:100px;height:2px;background:#333"></div>
    <p class="lead" style="position:absolute;top:105px;width:900px">We live in a digital world that is connected. We are here to make those connections, and help our customers succeed.<br>Whatever you need, large or small, we will strive to meet and exceed your expectations.</p>
    <div class="brand-small">Telmora Networks</div>
    <div class="features">
      <div class="feature"><div class="icon"><svg width="40" height="40" viewBox="0 0 40 40" fill="none" stroke="#fff" stroke-width="3"><circle cx="20" cy="20" r="7"/><path d="M20 3v6M20 31v6M3 20h6M31 20h6M8 8l4 4M28 28l4 4M32 8l-4 4M8 32l4-4"/></svg></div><h4>Our Solutions</h4><p>We provide complete wireless solutions for any size project, from simple links to full campus systems.</p></div>
      <div class="feature"><div class="icon"><svg width="40" height="40" viewBox="0 0 40 40" fill="#fff"><circle cx="20" cy="13" r="6"/><path d="M8 34c0-8 5-12 12-12s12 4 12 12z"/></svg></div><h4>Customer Focus</h4><p>Our customers are the heart of our work. We listen first and build networks around real needs.</p></div>
      <div class="feature"><div class="icon"><svg width="40" height="40" viewBox="0 0 40 40" fill="#fff"><path d="M13 18v-5a7 7 0 0114 0v5h-4v-5a3 3 0 00-6 0v5z"/><rect x="10" y="18" width="20" height="16" rx="2"/></svg></div><h4>Safety First</h4><p>Every crew is trained and certified to work safely on towers, rooftops and job sites.</p></div>
      <div class="feature"><div class="icon"><svg width="40" height="40" viewBox="0 0 40 40" fill="#fff"><circle cx="20" cy="12" r="6"/><path d="M9 34c0-9 5-13 11-13s11 4 11 13z"/><path d="M20 21l-2 6 2 4 2-4z" fill="#8cc63e"/></svg></div><h4>Professionalism</h4><p>Our team holds itself to the highest standard in planning, installation and ongoing support.</p></div>
      <div class="feature"><div class="icon"><svg width="40" height="40" viewBox="0 0 40 40" fill="#fff"><circle cx="20" cy="15" r="10"/><path d="M14 23l-3 13 9-5 9 5-3-13z"/></svg></div><h4>Quality</h4><p>We use proven equipment and careful workmanship so every network performs for years.</p></div>
    </div>
  </div>
</section>

<section class="projects on-dark">
  <div class="wrap">
    <h2 class="section-title" style="position:absolute;top:50px;width:900px">Our latest projects</h2>
    <p class="lead" style="position:absolute;top:96px;width:900px">Take a look at our latest projects and learn more about what we can do for you and your networking needs.</p>
    <div class="cards" style="top:143px">
      <div class="card project"><div class="img photo" role="img" aria-label="Rooftop antennas on a building" style="background:linear-gradient(180deg,#9fc2e3,#c9b59a)"></div><h3>Broadband 4.9 GHz / licensed PTP link</h3><p>This pair of radios delivers a high capacity backhaul link between two sites with room to grow.</p><a>Learn Project Details</a></div>
      <div class="card project"><div class="img photo" role="img" aria-label="Dish antenna on a red roof" style="background:linear-gradient(180deg,#b7cde0,#8e3a2c)"></div><h3>Dual broadband 4.9 GHz links</h3><p>Two links installed to provide redundancy for a city network serving public safety teams.</p><a>Learn Project Details</a></div>
      <div class="card project"><div class="img photo" role="img" aria-label="Communications tower with antennas" style="background:linear-gradient(180deg,#c7d9ea,#7b8a93)"></div><h3>Multi tenant condo WiFi and surveillance</h3><p>A resort condo complex now enjoys full wireless coverage and a modern camera system.</p><a>Learn Project Details</a></div>
    </div>
    <div class="arrows" style="top:525px">
      <div class="arrow"><svg width="10" height="14"><path d="M8 1L2 7l6 6" stroke="#fff" stroke-width="2" fill="none"/></svg></div>
      <div class="arrow"><svg width="10" height="14"><path d="M2 1l6 6-6 6" stroke="#fff" stroke-width="2" fill="none"/></svg></div>
    </div>
    <div class="dots" style="top:582px"><i class="dot on"></i><i class="dot"></i><i class="dot"></i><i class="dot"></i></div>
  </div>
</section>

<section class="team on-light">
  <div class="wrap">
    <h2 class="section-title" style="position:absolute;top:80px;width:900px">Meet our amazing team</h2>
    <p class="lead" style="position:absolute;top:128px;width:900px">Experience is what drives our team. With our combination of experience and knowledge, we can solve new<br>problems and provide you with knowledge to help you make decisions.</p>
    <div class="members">
      <div class="member"><div class="img" role="img" aria-label="Team member portrait"></div><h5>Arlen Voss</h5><small>CEO / Founder</small><div class="social"><i></i><i></i><i></i><i></i></div></div>
      <div class="member"><div class="img" role="img" aria-label="Team member portrait"></div><h5>Corin Voss</h5><small>VP of Sales and Marketing</small><div class="social"><i></i><i></i><i></i><i></i></div></div>
      <div class="member"><div class="img" role="img" aria-label="Team member portrait"></div><h5>Dell Marrick</h5><small>Sales Executive</small><div class="social"><i></i><i></i><i></i><i></i></div></div>
      <div class="member"><div class="img" role="img" aria-label="Team member portrait"></div><h5>Ruel Pastane</h5><small>Systems Engineer</small><div class="social"><i></i><i></i><i></i><i></i></div></div>
      <div class="member"><div class="img" role="img" aria-label="Team member portrait"></div><h5>Brayden Oakes</h5><small>Field Technician</small><div class="social"><i></i><i></i><i></i><i></i></div></div>
    </div>
    <div class="arrows" style="top:437px">
      <div class="arrow"><svg width="10" height="14"><path d="M8 1L2 7l6 6" stroke="#fff" stroke-width="2" fill="none"/></svg></div>
      <div class="arrow"><svg width="10" height="14"><path d="M2 1l6 6-6 6" stroke="#fff" stroke-width="2" fill="none"/></svg></div>
    </div>
    <div class="dots" style="top:494px"><i class="dot on"></i><i class="dot"></i><i class="dot"></i><i class="dot"></i><i class="dot"></i></div>
  </div>
</section>

<section class="banner" role="img" aria-label="Green tinted antenna tower backdrop">
  <p>As a customer driven company, the focus is to provide creative solutions paired with unparalleled technical and customer support. Today that focus has led to hundreds of clients who repeatedly turn to Telmora for their communications solutions.</p>
</section>

<section class="success on-dark" aria-label="Success stories">
  <div class="wrap">
    <h2 class="section-title" style="position:absolute;top:88px;width:900px">Success stories</h2>
    <div class="person photo" role="img" aria-label="Customer portrait"></div>
    <blockquote>What can we say but thank you to Arlen and Telmora Networks. We were able to quickly and effectively solve our WiFi problems. We had a very tight schedule to meet and they were able to get the results we wanted. Now several weeks later, we have logged more users and bandwidth usage on the network than ever before. As a result, our management has noted a dramatic decrease in the number of resident complaints about wireless connectivity. Today, the network handles hundreds of bandwidth hungry college students.</blockquote>
    <cite>Norris Elwin<small>Director of Student Housing and Facilities</small></cite>
    <div class="dots" style="top:470px"><i class="dot on"></i><i class="dot"></i><i class="dot"></i><i class="dot"></i></div>
  </div>
</section>

<section class="partners on-light">
  <div class="wrap">
    <h2 class="section-title" style="position:absolute;top:28px;width:900px">Our partners</h2>
    <p class="lead" style="position:absolute;top:72px;width:900px">Telmora Networks partners with the market leaders in networking technologies.<br>We are committed to delivering the right product for your exact needs.</p>
    <div class="badges">
      <div class="badge"><i></i></div><div class="badge"><i></i></div><div class="badge"><i></i></div>
      <div class="badge"><i></i></div><div class="badge"><i></i></div><div class="badge"><i></i></div>
    </div>
  </div>
</section>

<section class="contact on-dark" role="img" aria-label="Hillside landscape with a lattice tower under a cloudy sky">
  <div class="wrap">
    <h2 class="section-title" style="position:absolute;top:78px;width:900px">Contact us</h2>
    <p class="lead" style="position:absolute;top:128px;width:900px;color:#e2e7d6">Please complete the form below for more information</p>
    <div class="fields"><div class="field">Your name</div><div class="field">Your email</div><div class="field">Your phone</div></div>
    <div class="message">Your message</div>
    <div class="send">Send the message</div>
    <div class="info">
      <div class="info-item"><svg width="30" height="30" viewBox="0 0 30 30" fill="#fff"><path d="M8 3l5 6-3 3c2 4 4 6 8 8l3-3 6 5-3 4C14 26 4 16 4 6z"/></svg><div><h6>Phones</h6>Telephone: 970-555-0142<br>Toll Free: 888-555-0176<br>Fax: 970-555-0198</div></div>
      <div class="info-item"><svg width="30" height="30" viewBox="0 0 30 30" fill="#fff"><path d="M15 2a9 9 0 019 9c0 7-9 17-9 17S6 18 6 11a9 9 0 019-9z"/><circle cx="15" cy="11" r="3.5" fill="#3e5a33"/></svg><div><h6>Office Address</h6>Telmora Networks<br>418 Kestrel Way, Suite 2<br>Ridgeview, CO 00000</div></div>
      <div class="info-item"><svg width="30" height="30" viewBox="0 0 30 30"><rect x="3" y="7" width="24" height="16" fill="#fff"/><path d="M3 7l12 9 12-9" stroke="#3e5a33" stroke-width="2" fill="none"/></svg><div><h6>Email</h6>hello@4qvtelmora.com<br>www.4qvtelmora.com</div></div>
    </div>
  </div>
</section>

<footer>
  <div class="copy">Copyright © 2013 Telmora Networks, Inc. All Rights Reserved.</div>
  <div class="social"><i></i><i></i><i></i><i></i><i></i></div>
</footer>

</body>
</html>
```